Coastal waterside shopping complex needs a billboard sign

"Harbour Verge" is the name of a building which comprises 4 shops in a coastal waterside location. We need a 2440mm (Wide) x 1100mm (High) "Harbour Verge" billboard design that will fit with the coastal theme but is modern and contemporary, positioning the building as a high class mini shopping complex.

The photo below is for reference only. We only need a design for the "Harbour Verge" sign.

The end product will need to be an EPS scalable vector file.

```html
<!DOCTYPE html>
<html lang="en">
<head>
<meta charset="utf-8">
<title>Harbour Verge – Billboard</title>
<link rel="stylesheet" href="https://fonts.googleapis.com/css2?family=Poppins:wght@300;700&display=swap">
<style>
  :root {
    --canvas: #ffffff;
    --night: #0c1a22;
    --night-deep: #071218;
    --aqua: #00e3dc;
    --white: #ffffff;
    --mist: #d9e4e8;
    --ink: #0a0f12;
    --sea: #2a9ec9;
    --sand: #d8d8d4;
    --foliage: #2f7a35;
  }
  * { margin: 0; padding: 0; box-sizing: border-box; }
  html, body {
    width: 1200px; height: 1200px; overflow: hidden;
    background: var(--canvas);
  }
  .billboard {
    position: absolute;
    left: 50px; top: 352px;
    width: 1100px; height: 496px;
    overflow: hidden;
    box-shadow: 0 6px 14px rgba(0,0,0,0.35);
    font-family: "Poppins", sans-serif;
  }
  .billboard__photo {
    position: absolute; inset: 0;
    background:
      linear-gradient(200deg, var(--foliage) 0%, #3d8a3a 14%, var(--sand) 30%, #e8ecec 48%, #9fd3e6 60%, var(--sea) 78%, #1e6f95 100%);
  }
  .billboard__graphics {
    position: absolute; inset: 0;
    width: 100%; height: 100%;
  }
  .billboard__title {
    position: absolute;
    left: 74px; top: 48px;
    font-weight: 700;
    font-size: 132px;
    line-height: 172px;
    letter-spacing: -2px;
  }
  .billboard__title-top { display: block; color: var(--white); }
  .billboard__title-bottom { display: block; color: var(--aqua); }
  .billboard__tagline {
    position: absolute;
    left: 77px; top: 404px;
    font-weight: 300;
    font-size: 27px;
    color: var(--mist);
  }
  .billboard__mark {
    position: absolute;
    left: 985px; top: 437px;
    font-weight: 700;
    font-size: 21px;
    line-height: 23px;
    color: var(--ink);
  }
</style>
</head>
<body>
  <div class="billboard">
    <div class="billboard__photo" role="img" aria-label="Aerial view of a tropical shoreline: dark ocean water, white surf, a sandy beach and green palm trees"></div>

    <svg class="billboard__graphics" viewBox="0 0 1050 474" preserveAspectRatio="none" aria-hidden="true">
      <defs>
        <linearGradient id="panelShade" x1="0" y1="0" x2="1" y2="1">
          <stop offset="0" stop-color="#0e1c24" stop-opacity="0.97"/>
          <stop offset="1" stop-color="#06141b" stop-opacity="0.95"/>
        </linearGradient>
      </defs>
      <polygon class="dark-panel" points="0,0 885,0 565,474 0,474" fill="url(#panelShade)"/>
      <polygon class="stripe stripe--aqua" points="765,222 805,222 625,474 585,474" fill="var(--aqua)"/>
      <polygon class="stripe stripe--white" points="770,322 805,322 715,474 655,474" fill="var(--white)"/>
      <polygon class="stripe stripe--dark" points="765,412 810,412 775,474 725,474" fill="var(--night-deep)"/>
    </svg>

    <h1 class="billboard__title">
      <span class="billboard__title-top">Harbour</span>
      <span class="billboard__title-bottom">Verge</span>
    </h1>
    <p class="billboard__tagline">mini shopping complex</p>
    <div class="billboard__mark">Harbour<br>Verge</div>
  </div>
</body>
</html>
```